Webdesign für Branchenverzeichnis
Zielgruppe
Wir-bauen-Brücken – das Branchenverzeichnis der Selbstverantwortlichen.
Der Anbieter präsentiert sich mit seinem Namen und der URL - ähnlich wie bei 'blaue Blätter' oder Torkwerk.
Aufgabenstellung
Das Branchenverzeichnis sollte neutral und gleichzeitig hochwertig sein. Die Hauptfarben sind Gold, Schwarz und Weiß. Logo und Corporate Design wurden bereits entwickelt

```html
<!DOCTYPE html>
<html lang="de">
<head>
<meta charset="utf-8">
<title>Wir-bauen-Brücken – Suchen</title>
<link rel="stylesheet" href="https://fonts.googleapis.com/css2?family=Quicksand:wght@400;500;600;700&display=swap">
<style>
:root{
  --gold:#d4b063;
  --gold-light:#e2c37e;
  --ink:#111111;
  --dark:#3a3a3a;
  --cream:#fdfbef;
  --card:#faf5d6;
  --card-border:#e6d59a;
  --muted:#6b6b6b;
  --white:#ffffff;
  --map:#d8e4dc;
}
*{box-sizing:border-box;margin:0;padding:0}
html,body{width:1025px;height:1200px;overflow:hidden}
body{position:relative;background:var(--cream);font-family:"Quicksand",sans-serif;color:var(--ink)}
.abs{position:absolute}

.topbar{left:0;top:0;width:1025px;height:53px;background:linear-gradient(#555,#2f2f2f)}
.brand{left:128px;top:11px;width:56px;display:flex;align-items:center;gap:4px;color:var(--gold);font-size:8px;font-weight:700;line-height:1.1}
.brand .dot{width:9px;height:9px;border-radius:50%;border:1.5px solid var(--gold);flex:none}
.nav a{position:absolute;top:22px;font-size:7.5px;font-weight:700;letter-spacing:1px;color:var(--white);text-decoration:none}
.nav a.active{color:var(--gold)}
.flag{left:703px;top:16px;width:22px;height:21px;border:1px solid var(--gold);padding:5px 3px}
.flag span{display:block;height:3.6px}
.account{left:732px;top:16px;width:21px;height:21px;border:1px solid var(--gold);display:flex;align-items:center;justify-content:center}
.cta{left:785px;top:15px;width:106px;height:24px;background:var(--gold);color:var(--white);font-size:7px;font-weight:600;letter-spacing:.8px;display:flex;align-items:center;justify-content:center}

.headline{left:0;top:92px;width:1025px;text-align:center;font-size:20px;font-weight:700;letter-spacing:3px}
.headline em{font-style:normal;color:var(--gold)}
.lead{left:0;top:124px;width:1025px;text-align:center;font-size:9px;letter-spacing:.8px}

.searchband{left:141px;top:155px;width:758px;height:80px;background:var(--gold);box-shadow:0 6px 14px rgba(0,0,0,.12)}
.field{position:absolute;top:24px;width:160px;height:32px;background:var(--white);border:1px solid #e9dcb4;font-size:9.5px;color:#555;padding:0 11px;display:flex;align-items:center;justify-content:space-between}
.search-btn{position:absolute;left:620px;top:24px;width:106px;height:32px;background:var(--dark);color:var(--white);font-size:7.5px;font-weight:600;letter-spacing:.5px;display:flex;align-items:center;justify-content:center}

.result-title{left:142px;top:253px;font-size:11.5px;color:#333}
.result-title span{color:var(--gold)}
.result-count{left:142px;top:272px;font-size:8px;color:var(--muted);letter-spacing:.3px}
.sort-label{left:446px;top:272px;font-size:8px;color:var(--muted)}
.sort{left:514px;top:268px;width:81px;height:18px;border:1px solid #ddd;background:var(--white);font-size:6px;color:#999;padding:0 8px;display:flex;align-items:center;justify-content:space-between}
.divider{left:142px;top:293px;width:453px;height:1px;background:#ddd}

.card{position:absolute;left:142px;width:453px;height:64px;background:var(--card);border:1px solid var(--card-border);box-shadow:0 2px 6px rgba(0,0,0,.06)}
.card-logo{position:absolute;left:14px;top:20px;width:52px;display:flex;align-items:center;gap:3px;color:var(--gold);font-size:6.5px;font-weight:700;line-height:1.15}
.card-logo .dot{width:7px;height:7px;border-radius:50%;border:1.2px solid var(--gold);flex:none}
.card-name{position:absolute;left:96px;top:16px;font-size:12px;font-weight:500;letter-spacing:.8px}
.card-meta{position:absolute;left:96px;top:36px;display:flex;gap:24px;font-size:6.5px;color:var(--muted);letter-spacing:.3px}
.card-meta span{display:flex;align-items:center;gap:3px}
.card-btn{position:absolute;left:370px;top:20px;width:67px;height:22px;border:1px solid var(--dark);font-size:6.5px;letter-spacing:.6px;color:var(--muted);display:flex;align-items:center;justify-content:center}
.card-btn.filled{background:var(--dark);color:var(--white)}

.map{left:639px;top:332px;width:260px;height:528px;background:linear-gradient(160deg,#e6e3da 0%,#dfe1d8 45%,#b9d6e0 80%,#a9cfdd 100%)}

.page{position:absolute;top:898px;width:27px;height:27px;border:1px solid var(--gold);font-size:10px;display:flex;align-items:center;justify-content:center;color:#555}
.page.current{color:var(--gold);font-weight:700}

.footer{left:0;top:970px;width:1025px;height:230px;background:linear-gradient(#6a6a6a,#2a2a2a)}
.footer-brand{left:214px;top:1050px;width:62px;display:flex;align-items:center;gap:4px;color:var(--gold);font-size:9px;font-weight:700;line-height:1.15}
.footer-brand .dot{width:10px;height:10px;border-radius:50%;border:1.5px solid var(--gold);flex:none}
.footer h4{position:absolute;font-size:10px;font-weight:700;color:var(--gold);letter-spacing:.5px}
.footer p,.footer a{position:absolute;font-size:8px;color:var(--gold);line-height:13.5px;text-decoration:none}
.footer .about{text-decoration:underline}
.copy{left:0;top:1176px;width:1025px;text-align:center;font-size:6.5px;font-weight:600;color:var(--gold)}
</style>
</head>
<body>

<header class="abs topbar">
  <div class="abs brand"><span class="dot"></span>Wir-bauen-Brücken</div>
  <nav class="nav">
    <a style="left:245px">HOME</a>
    <a class="active" style="left:310px">SUCHEN</a>
    <a style="left:384px">ÜBER UNS</a>
    <a style="left:465px">MITGLIEDSCHAFT</a>
    <a style="left:577px">KONTAKT</a>
  </nav>
  <div class="abs flag"><span style="background:#000"></span><span style="background:#d00"></span><span style="background:#fc0"></span></div>
  <div class="abs account"><svg width="10" height="10" viewBox="0 0 10 10"><circle cx="5" cy="3" r="2.2" fill="#d4b063"/><path d="M1 10c0-3 2-4.5 4-4.5s4 1.5 4 4.5z" fill="#d4b063"/></svg></div>
  <div class="abs cta">MITGLIED WERDEN</div>
</header>

<h1 class="abs headline">WIR ZEIGEN <em>UNTERNEHMER</em></h1>
<p class="abs lead">Suche in deiner Region und finde neue Unternehmen in vielen Branchen &amp; Ländern.</p>

<section class="abs searchband">
  <div class="field" style="left:33px">Unternehmen, Name
    <svg width="15" height="13" viewBox="0 0 15 13"><path d="M7.5 0L15 6.5h-2V13H9V9H6v4H2V6.5H0z" fill="#d4b063"/></svg></div>
  <div class="field" style="left:219px">Stadt, PLZ oder Land
    <svg width="15" height="15" viewBox="0 0 15 15"><circle cx="7.5" cy="7.5" r="5" fill="none" stroke="#d4b063" stroke-width="1.5"/><circle cx="7.5" cy="7.5" r="2.3" fill="#d4b063"/><path d="M7.5 0v2.5M7.5 12.5V15M0 7.5h2.5M12.5 7.5H15" stroke="#d4b063" stroke-width="1.5"/></svg></div>
  <div class="field" style="left:406px">Branche
    <svg width="11" height="7" viewBox="0 0 11 7"><path d="M1 1l4.5 4.5L10 1" fill="none" stroke="#d4b063" stroke-width="1.5"/></svg></div>
  <div class="search-btn">SUCHEN</div>
</section>

<p class="abs result-title">Ihre Suchergebnisse für: <span>IT &amp; Marketing</span></p>
<p class="abs result-count">Zeige 7 von 25 Brancheneinträgen</p>
<p class="abs sort-label">Sortieren nach</p>
<div class="abs sort">Firmenname A-Z <svg width="8" height="5" viewBox="0 0 8 5"><path d="M.5.5L4 4 7.5.5" fill="none" stroke="#999"/></svg></div>
<div class="abs divider"></div>

<main>
  <article class="card" style="top:332px">
    <div class="card-logo"><span class="dot"></span>Wir-bauen-Brücken</div>
    <h2 class="card-name">Firmenname Karl Berger Consulting</h2>
    <div class="card-meta"><span><svg width="6" height="6"><rect x=".5" y=".5" width="5" height="5" fill="none" stroke="#d4b063"/></svg>IT &amp; Marketing</span><span><svg width="5" height="7" viewBox="0 0 5 7"><path d="M2.5 7L.3 3.2A2.5 2.5 0 1 1 4.7 3.2z" fill="#d4b063"/></svg>München</span></div>
    <div class="card-btn filled">ZUR WEBSITE</div>
  </article>
  <article class="card" style="top:409px">
    <div class="card-logo"><span class="dot"></span>Wir-bauen-Brücken</div>
    <h2 class="card-name">Firmenname Karl Berger Consulting</h2>
    <div class="card-meta"><span><svg width="6" height="6"><rect x=".5" y=".5" width="5" height="5" fill="none" stroke="#d4b063"/></svg>IT &amp; Marketing</span><span><svg width="5" height="7" viewBox="0 0 5 7"><path d="M2.5 7L.3 3.2A2.5 2.5 0 1 1 4.7 3.2z" fill="#d4b063"/></svg>München</span></div>
    <div class="card-btn">ZUR WEBSITE</div>
  </article>
  <article class="card" style="top:487px">
    <div class="card-logo"><span class="dot"></span>Wir-bauen-Brücken</div>
    <h2 class="card-name">Firmenname Karl Berger Consulting</h2>
    <div class="card-meta"><span><svg width="6" height="6"><rect x=".5" y=".5" width="5" height="5" fill="none" stroke="#d4b063"/></svg>IT &amp; Marketing</span><span><svg width="5" height="7" viewBox="0 0 5 7"><path d="M2.5 7L.3 3.2A2.5 2.5 0 1 1 4.7 3.2z" fill="#d4b063"/></svg>München</span></div>
    <div class="card-btn">ZUR WEBSITE</div>
  </article>
  <article class="card" style="top:564px">
    <div class="card-logo"><span class="dot"></span>Wir-bauen-Brücken</div>
    <h2 class="card-name">Firmenname Karl Berger Consulting</h2>
    <div class="card-meta"><span><svg width="6" height="6"><rect x=".5" y=".5" width="5" height="5" fill="none" stroke="#d4b063"/></svg>IT &amp; Marketing</span><span><svg width="5" height="7" viewBox="0 0 5 7"><path d="M2.5 7L.3 3.2A2.5 2.5 0 1 1 4.7 3.2z" fill="#d4b063"/></svg>München</span></div>
    <div class="card-btn">ZUR WEBSITE</div>
  </article>
  <article class="card" style="top:641px">
    <div class="card-logo"><span class="dot"></span>Wir-bauen-Brücken</div>
    <h2 class="card-name">Firmenname Karl Berger Consulting</h2>
    <div class="card-meta"><span><svg width="6" height="6"><rect x=".5" y=".5" width="5" height="5" fill="none" stroke="#d4b063"/></svg>IT &amp; Marketing</span><span><svg width="5" height="7" viewBox="0 0 5 7"><path d="M2.5 7L.3 3.2A2.5 2.5 0 1 1 4.7 3.2z" fill="#d4b063"/></svg>München</span></div>
    <div class="card-btn">ZUR WEBSITE</div>
  </article>
  <article class="card" style="top:719px">
    <div class="card-logo"><span class="dot"></span>Wir-bauen-Brücken</div>
    <h2 class="card-name">Firmenname Karl Berger Consulting</h2>
    <div class="card-meta"><span><svg width="6" height="6"><rect x=".5" y=".5" width="5" height="5" fill="none" stroke="#d4b063"/></svg>IT &amp; Marketing</span><span><svg width="5" height="7" viewBox="0 0 5 7"><path d="M2.5 7L.3 3.2A2.5 2.5 0 1 1 4.7 3.2z" fill="#d4b063"/></svg>München</span></div>
    <div class="card-btn">ZUR WEBSITE</div>
  </article>
  <article class="card" style="top:796px">
    <div class="card-logo"><span class="dot"></span>Wir-bauen-Brücken</div>
    <h2 class="card-name">Firmenname Karl Berger Consulting</h2>
    <div class="card-meta"><span><svg width="6" height="6"><rect x=".5" y=".5" width="5" height="5" fill="none" stroke="#d4b063"/></svg>IT &amp; Marketing</span><span><svg width="5" height="7" viewBox="0 0 5 7"><path d="M2.5 7L.3 3.2A2.5 2.5 0 1 1 4.7 3.2z" fill="#d4b063"/></svg>München</span></div>
    <div class="card-btn">ZUR WEBSITE</div>
  </article>
</main>

<div class="abs map" role="img" aria-label="Stadtplan mit Standortmarkierungen der Suchergebnisse"></div>

<nav class="pagination">
  <div class="page current" style="left:291px">1</div>
  <div class="page" style="left:323px">2</div>
  <div class="page" style="left:355px">3</div>
  <div class="page" style="left:387px">4</div>
  <div class="page" style="left:419px">5</div>
</nav>

<footer class="abs footer"></footer>
<div class="footer">
  <div class="abs footer-brand"><span class="dot"></span>Wir-bauen-Brücken</div>
  <h4 style="left:307px;top:1036px">Wir bauen Brücken</h4>
  <p style="left:307px;top:1059px;width:165px">Duis sed odio sit amet nibh vulputate cursus a sit amet mauris. Morbi accumsan ipsum velit. Nam nec tellus a</p>
  <a class="about" style="left:307px;top:1103px">Über uns</a>
  <h4 style="left:553px;top:1035px">WEBSITE</h4>
  <a style="left:553px;top:1059px">Wir bauen Brücken</a>
  <a style="left:553px;top:1080px">Unternehmen suchen</a>
  <a style="left:553px;top:1102px">Mitgliedschaft</a>
  <a style="left:553px;top:1123px">Kontakt</a>
  <h4 style="left:717px;top:1035px">RECHTLICHES</h4>
  <a style="left:717px;top:1059px">Impressum</a>
  <a style="left:717px;top:1080px">Datenschutz</a>
  <a style="left:717px;top:1102px">AGB</a>
  <a style="left:717px;top:1123px">Sicherheitsbestimmungen</a>
  <p class="abs copy" style="position:absolute">© 2020 Wir Bauen Brücken</p>
</div>

</body>
</html>
```